Talvin Foundation Letterhead

We are a newly established non profit registered in Maryland but operates in Africa, south of the sahara. We offer scholarships to deserving young adults from high school through college. Our color theme for our existing logo is purple, we want a design that is stylish, spellbinding yet a letterhead that projects seriousness. More information on www.thetalvinfoundation.example

Target Market(s)

High school and college students in sub saharan African as well as our donors in the US

Industry/Entity Type

Non Profit

Font styles to use
Script

Requirements
Must have
• Logo at the top and if possible watermark the logo in the middle of the letterhead, contact address,
Should not have
• NA

```html
<!DOCTYPE html>
<html lang="en">
<head>
<meta charset="utf-8">
<title>Talvin Foundation Letterhead</title>
<link rel="stylesheet" href="https://fonts.googleapis.com/css2?family=Cabin:ital,wght@0,400;0,500;1,400&family=Cormorant+SC:wght@500;600&display=swap">
<style>
  :root {
    --backdrop: #dcdcdc;
    --paper: #ffffff;
    --purple-deep: #5c2d91;
    --purple-soft: #9a64b8;
    --purple-text: #6b2fa0;
    --ink: #3a3a3a;
    --ink-muted: #555555;
    --watermark: #f1ecf6;
  }
  * { box-sizing: border-box; margin: 0; padding: 0; }
  html, body {
    width: 1200px; height: 1200px; overflow: hidden;
    background: var(--backdrop);
  }
  .letterhead {
    position: absolute; left: 211px; top: 50px;
    width: 778px; height: 1100px;
    background: var(--paper);
    box-shadow: 0 6px 24px rgba(0,0,0,0.12);
    overflow: hidden;
    font-family: "Cabin", sans-serif;
    color: var(--ink);
  }
  .wave { position: absolute; left: 0; top: 0; width: 778px; height: 1100px; }
  .brand {
    position: absolute; left: 250px; top: 56px;
    display: flex; align-items: center; gap: 12px;
  }
  .brand-mark {
    width: 34px; height: 34px; border-radius: 50%;
    background: var(--purple-deep);
  }
  .brand-name {
    font-family: "Cabin", sans-serif; font-weight: 500;
    font-size: 22px; letter-spacing: 1px; color: var(--purple-text);
    text-transform: uppercase;
  }
  .brand-tagline {
    position: absolute; left: 296px; top: 98px;
    font-size: 8px; letter-spacing: 1.2px; color: var(--purple-soft);
    text-transform: uppercase;
  }
  .sender { position: absolute; left: 110px; top: 170px; }
  .person-name {
    font-family: "Cormorant SC", serif; font-weight: 600;
    font-size: 18px; color: var(--purple-text); letter-spacing: .5px;
  }
  .person-role, .person-place { font-size: 12.5px; color: var(--ink-muted); line-height: 1.45; font-style: italic; }
  .contact {
    position: absolute; right: 48px; top: 160px;
    list-style: none; font-size: 13px; color: var(--purple-text); line-height: 1.2;
  }
  .contact li { display: flex; align-items: flex-start; gap: 8px; margin-bottom: 8px; }
  .contact svg { flex: none; width: 16px; height: 16px; }
  .letter-body {
    position: absolute; left: 110px; top: 268px; width: 440px;
    font-size: 12.5px; line-height: 1.55; color: var(--ink);
  }
  .letter-body p { margin-bottom: 14px; }
  .signoff { position: absolute; left: 110px; top: 640px; }
  .signature {
    width: 110px; height: 38px; margin-bottom: 4px;
    background: linear-gradient(90deg, #ece3f4, #d9c7ea);
    border-radius: 4px;
  }
</style>
</head>
<body>
  <main class="letterhead">
    <svg class="wave" viewBox="0 0 778 1100" aria-hidden="true">
      <circle cx="340" cy="830" r="190" fill="none" stroke="var(--watermark)" stroke-width="14"/>
      <path d="M0 780 C120 790 170 890 300 950 C450 1015 640 1025 778 1018 L778 1100 L0 1100 Z" fill="var(--purple-soft)"/>
      <path d="M0 798 C115 808 165 908 300 968 C450 1032 640 1040 778 1034 L778 1100 L0 1100 Z" fill="var(--purple-deep)"/>
    </svg>

    <header>
      <div class="brand">
        <span class="brand-mark"></span>
        <span class="brand-name">Talvin Foundation</span>
      </div>
      <div class="brand-tagline">Empowering young minds through the gift of education</div>
    </header>

    <section class="sender">
      <div class="person-name">Dana Whitfield</div>
      <div class="person-role">CEO &amp; Director</div>
      <div class="person-place">Washington, USA</div>
    </section>

    <ul class="contact">
      <li>
        <svg viewBox="0 0 16 16"><circle cx="8" cy="8" r="7.5" fill="none" stroke="var(--purple-soft)"/><path d="M5.5 4.5l1.5 1.5-1 1c.6 1.3 1.6 2.3 2.9 2.9l1-1 1.5 1.5-1.2 1.2C7.7 11.4 4.6 8.3 4.3 5.7z" fill="var(--purple-deep)"/></svg>
        <span>(+55) 50000 1234</span>
      </li>
      <li>
        <svg viewBox="0 0 16 16"><circle cx="8" cy="8" r="7.5" fill="none" stroke="var(--purple-soft)"/><rect x="4.5" y="5.5" width="7" height="5" fill="var(--purple-deep)"/><path d="M4.5 5.5l3.5 2.6 3.5-2.6" fill="none" stroke="#fff" stroke-width=".8"/></svg>
        <span>admin@thetalvinfoundation.example</span>
      </li>
      <li>
        <svg viewBox="0 0 16 16"><circle cx="8" cy="8" r="7.5" fill="none" stroke="var(--purple-soft)"/><path d="M8 3.8a2.6 2.6 0 0 1 2.6 2.6C10.6 8.5 8 11.8 8 11.8S5.4 8.5 5.4 6.4A2.6 2.6 0 0 1 8 3.8z" fill="var(--purple-deep)"/><circle cx="8" cy="6.4" r=".9" fill="#fff"/></svg>
        <span>48(B), Maple Crossing,<br>Washington, USA</span>
      </li>
    </ul>

    <article class="letter-body">
      <p>Lorem ipsum dolor sit amet, consectetur adipiscing elit. Nullam blandit lectus at justo sagittis semper. Cum sociis natoque penatibus et magnis dis parturient montes, nascetur ridiculus mus. Suspendisse porta, justo eu tempus suscipit, metus lorem bibendum enim, quis bibendum dolor leo nec nunc. Donec egestas a orci nec pharetra.</p>
      <p>Lorem ipsum dolor sit amet, consectetur adipiscing elit. Proin sed porta erat, vel dignissim urna. Vivamus quis nibh facilisis, scelerisque nulla ut, porttitor ante. Vivamus dapibus purus ut erat cursus, nec condimentum ante laoreet. Vivamus egestas ex eget augue molestie, a finibus leo consectetur. Fusce dictum ullamcorper suscipit.</p>
      <p>Vestibulum pellentesque turpis eget semper volutpat. Nam mi ante, laoreet vel auctor at, consectetur vel nisi. Integer tristique neque non mi auctor pulvinar. Phasellus blandit mauris vitae massa aliquet pharetra. Sed sit amet ultricies nulla, quis malesuada urna. Praesent non sagittis leo, at facilisis dolor. Suspendisse convallis ornare massa, a commodo diam pulvinar eget. Donec tincidunt finibus ante vitae imperdiet.</p>
    </article>

    <section class="signoff">
      <div class="signature" role="img" aria-label="Handwritten signature of the founder"></div>
      <div class="person-name">Marcus Ellery</div>
      <div class="person-role">Founder</div>
      <div class="person-place">Washington, USA</div>
    </section>
  </main>
</body>
</html>
```